Brasko Construction Business Card

I need a business card design for my company.
We are a construction/machinery company.
I would like to see my logo on the front of the card and my details on the other side
I would like the card to be black or dark grey in colour,with my logo as i send it or modified with a lighter blue colour
I would like to see the design kept fairly simple,but eye catching at the same time
Industry/Entity Type
Business
Contact Information for Business Card
Name
Phone Number
Address
Email
Colors
00a990
1b1b1b
000000
474747
ececec

```html
<!DOCTYPE html>
<html lang="en">
<head>
<meta charset="utf-8">
<title>Brasko Construction Business Card</title>
<link rel="stylesheet" href="https://fonts.googleapis.com/css2?family=Open+Sans:wght@400;600;700&display=swap">
<style>
  :root {
    --page-bg: #3a3532;
    --card-bg: #232323;
    --card-edge: #1b1b1b;
    --accent-blue: #2a9fd8;
    --text-light: #ececec;
    --text-muted: #d6d6d6;
    --icon-ink: #232323;
  }
  * { margin: 0; padding: 0; box-sizing: border-box; }
  html, body {
    width: 1200px;
    height: 780px;
    overflow: hidden;
    background: var(--page-bg);
    font-family: "Open Sans", Arial, sans-serif;
  }
  .sheet {
    position: relative;
    width: 1200px;
    height: 780px;
  }
  .card {
    position: absolute;
    width: 520px;
    height: 300px;
    background: var(--card-bg);
    border: 1px solid var(--card-edge);
    box-shadow: 0 10px 30px rgba(0,0,0,0.45);
  }
  .card--front { left: 50px; top: 120px; }
  .card--back { left: 630px; top: 360px; }

  .brand-mark {
    display: flex;
    align-items: center;
    gap: 10px;
    color: var(--accent-blue);
    font-weight: 700;
    text-transform: uppercase;
    letter-spacing: 1px;
    white-space: nowrap;
  }
  .brand-mark__square {
    width: 22px;
    height: 22px;
    background: var(--accent-blue);
    flex: none;
  }

  .card--front .brand-mark {
    position: absolute;
    left: 0; right: 0; top: 112px;
    justify-content: center;
    font-size: 26px;
  }
  .front-url {
    position: absolute;
    left: 0; right: 0; top: 180px;
    text-align: center;
    color: var(--accent-blue);
    font-size: 15px;
  }

  .card--back .brand-mark {
    position: absolute;
    right: 40px; top: 70px;
    font-size: 22px;
  }
  .contact-block {
    position: absolute;
    left: 24px; right: 24px; top: 170px;
    display: flex;
    justify-content: center;
    gap: 14px;
  }
  .identity {
    text-align: right;
    color: var(--text-muted);
    font-size: 13px;
    line-height: 1.45;
    white-space: nowrap;
  }
  .identity__name {
    color: var(--text-light);
    font-size: 20px;
    font-weight: 600;
    margin-bottom: 2px;
  }
  .divider {
    width: 2px;
    background: var(--accent-blue);
  }
  .contact-list { list-style: none; }
  .contact-list__item {
    display: flex;
    align-items: center;
    gap: 8px;
    color: var(--text-light);
    font-size: 14px;
    font-weight: 600;
    line-height: 24px;
    white-space: nowrap;
  }
  .contact-icon {
    width: 17px;
    height: 17px;
    background: var(--accent-blue);
    display: flex;
    align-items: center;
    justify-content: center;
    flex: none;
  }
  .contact-icon svg { width: 12px; height: 12px; }
</style>
</head>
<body>
<main class="sheet">
  <section class="card card--front" aria-label="Card front">
    <div class="brand-mark"><span class="brand-mark__square"></span>Brasko Construction</div>
    <p class="front-url">www.braskobuild.com</p>
  </section>

  <section class="card card--back" aria-label="Card back">
    <div class="brand-mark"><span class="brand-mark__square"></span>Brasko Construction</div>
    <div class="contact-block">
      <div class="identity">
        <p class="identity__name">Employee Name</p>
        <p>P.O. Box 214, Elm Street</p>
        <p>Ridgefield Vale, USA</p>
      </div>
      <span class="divider"></span>
      <ul class="contact-list">
        <li class="contact-list__item">
          <span class="contact-icon">
            <svg viewBox="0 0 12 12"><path d="M3 1 L5 3.5 L4 4.8 Q5 7 7.2 8 L8.5 7 L11 9 L9.8 11 Q4.5 10.5 1 3 Z" fill="var(--icon-ink)"/></svg>
          </span>0456 782 310
        </li>
        <li class="contact-list__item">
          <span class="contact-icon">
            <svg viewBox="0 0 12 12"><rect x="1" y="2.5" width="10" height="7" fill="none" stroke="var(--icon-ink)" stroke-width="1.2"/><path d="M1 2.5 L6 6.5 L11 2.5" fill="none" stroke="var(--icon-ink)" stroke-width="1.2"/></svg>
          </span>info@braskomail.net.au
        </li>
        <li class="contact-list__item">
          <span class="contact-icon">
            <svg viewBox="0 0 12 12"><circle cx="6" cy="6" r="4.6" fill="none" stroke="var(--icon-ink)" stroke-width="1.1"/><ellipse cx="6" cy="6" rx="2" ry="4.6" fill="none" stroke="var(--icon-ink)" stroke-width="1"/><path d="M1.4 6 H10.6" stroke="var(--icon-ink)" stroke-width="1"/></svg>
          </span>www.braskobuild.com
        </li>
      </ul>
    </div>
  </section>
</main>
</body>
</html>
```